Skin care products for Men Label design

I am looking for a designer, who can help with the label design for my new skin care products line for Men.
Modern design, with a manly feel for ecology products.
Colors that must be included:
Black and Blue (see company logo in uploaded files)

These are the measurements:

Cleanser: MM: 130 x 60

Skintonic : MM:130 x 60

Day Creme: MM 105 x 74

Target Market(s)

Men aged 25-55

Industry/Entity Type

Skin Care Product

Requirements
Must have
• Colors that must be included:

```html
<!DOCTYPE html>
<html lang="en">
<head>
<meta charset="utf-8">
<title>Iron Ridge Skintonic Label</title>
<link href="https://fonts.googleapis.com/css2?family=Anton&family=Exo+2:wght@600&family=Roboto:wght@700&display=swap" rel="stylesheet">
<style>
  :root {
    --page: #ffffff;
    --kraft: #d6b590;
    --kraft-dark: #c9a67f;
    --ink: #262626;
    --panel: #2d2d2d;
    --blue: #3f6c9c;
    --blue-deep: #355e8a;
    --white: #ffffff;
  }
  html, body {
    margin: 0;
    padding: 0;
    width: 1200px;
    height: 1152px;
    overflow: hidden;
    background: var(--page);
  }
  .label {
    position: absolute;
    left: 385px;
    top: 166px;
    width: 430px;
    height: 820px;
    background: radial-gradient(circle at 30% 40%, var(--kraft) 0%, var(--kraft-dark) 100%);
    overflow: hidden;
  }
  .brand-panel {
    position: absolute;
    left: 28px;
    top: 6px;
    width: 209px;
    height: 190px;
    background: var(--panel);
    display: flex;
    align-items: flex-end;
    justify-content: center;
    padding-bottom: 30px;
    box-sizing: border-box;
  }
  .brand-name {
    font-family: "Roboto", sans-serif;
    font-weight: 700;
    font-size: 22px;
    color: var(--white);
  }
  .splash-art {
    position: absolute;
    left: 0;
    top: 316px;
    width: 249px;
    height: 396px;
    background: radial-gradient(ellipse at 40% 35%, var(--blue) 0%, var(--blue) 45%, rgba(63,108,156,0.35) 75%, rgba(63,108,156,0) 100%);
  }
  .headline {
    position: absolute;
    left: 34px;
    margin: 0;
    font-family: "Anton", sans-serif;
    font-weight: 400;
    font-size: 118px;
    line-height: 1;
    color: var(--ink);
    letter-spacing: 2px;
  }
  .headline-for { top: 218px; }
  .headline-men { top: 355px; }
  .side-band {
    position: absolute;
    left: 269px;
    top: 0;
    width: 82px;
    height: 100%;
    background: linear-gradient(90deg, var(--blue) 0%, var(--blue-deep) 100%);
  }
  .product-name {
    position: absolute;
    left: 362px;
    top: 22px;
    width: 68px;
    height: 770px;
    margin: 0;
    writing-mode: vertical-rl;
    font-family: "Exo 2", sans-serif;
    font-weight: 600;
    font-size: 68px;
    line-height: 68px;
    letter-spacing: 24px;
    text-transform: uppercase;
    color: var(--ink);
  }
  .volume {
    position: absolute;
    left: 54px;
    top: 748px;
    font-family: "Exo 2", sans-serif;
    font-weight: 600;
    font-size: 36px;
    letter-spacing: 4px;
    color: var(--ink);
  }
</style>
</head>
<body>
  <div class="label">
    <div class="brand-panel">
      <span class="brand-name">Iron Ridge</span>
    </div>
    <div class="splash-art" role="img" aria-label="Blue paint splash texture behind the headline"></div>
    <h1 class="headline headline-for">FOR</h1>
    <h1 class="headline headline-men">MEN</h1>
    <div class="side-band"></div>
    <h2 class="product-name">Skintonic</h2>
    <div class="volume">250ML</div>
  </div>
</body>
</html>
```